Innovative Fashion Business needs Branding and Business Card.

We need a Business Card and Branding work (Email Footer, Stickers, letterhead, all from same Design) We are an innovative, progressive and exciting Fashion Start-up. We are called "Moss Tide" I am attaching the original artwork of the image I want to use. Also have a previous Card, I want to do something like that, only using this new image.

```html
<!DOCTYPE html>
<html lang="en">
<head>
<meta charset="utf-8">
<title>Moss Tide — Business Card</title>
<link rel="stylesheet" href="https://fonts.googleapis.com/css2?family=Arimo:wght@400;700&display=swap">
<style>
  :root {
    --backdrop: #e6e4e8;
    --card: #ffffff;
    --ink: #111111;
    --accent: #b77fb0;
    --art-cream: #fbf1d8;
    --art-peach: #f3d9b4;
    --art-lilac: #c9a3cf;
    --art-violet: #7a5a9c;
    --shadow: rgba(0, 0, 0, 0.18);
  }
  * { box-sizing: border-box; margin: 0; padding: 0; }
  html, body {
    width: 1200px; height: 903px; overflow: hidden;
    background: var(--backdrop);
    font-family: "Arimo", Arial, sans-serif;
    color: var(--ink);
  }
  .sheet { position: relative; width: 1200px; height: 903px; }
  .card {
    position: absolute; left: 260px; width: 680px; height: 389px;
    background: var(--card);
    box-shadow: 0 6px 22px var(--shadow);
  }
  .card--front { top: 52px; }
  .card--back { top: 462px; text-align: center; }

  /* front */
  .wordmark {
    position: absolute; left: 120px; top: 40px;
    font-size: 56px; font-weight: 400; letter-spacing: 1px;
    color: var(--ink); line-height: 1;
  }
  .artwork {
    position: absolute; left: 150px; top: 108px; width: 400px; height: 208px;
    border-radius: 6px;
    background:
      radial-gradient(ellipse at 70% 35%, var(--art-peach) 0%, transparent 60%),
      radial-gradient(ellipse at 45% 95%, var(--art-lilac) 0%, transparent 55%),
      linear-gradient(160deg, var(--card) 0%, var(--art-cream) 45%, var(--art-lilac) 100%);
  }
  .artwork__band {
    position: absolute; left: 40px; bottom: 18px; width: 150px; height: 10px;
    background: var(--art-violet); border-radius: 5px; opacity: .8;
  }
  .tagline {
    position: absolute; left: 0; right: 0; top: 332px;
    text-align: center; font-size: 19px; letter-spacing: .3px;
  }

  /* back */
  .holder__name { margin-top: 58px; font-size: 34px; font-weight: 700; }
  .holder__role { margin-top: 4px; font-size: 21px; color: var(--accent); }
  .divider { display: block; margin: 12px auto; }
  .services { font-size: 21px; line-height: 1.3; }
  .contact { font-size: 22px; line-height: 1.35; }
</style>
</head>
<body>
<main class="sheet">
  <section class="card card--front" aria-label="Card front">
    <div class="wordmark">MOSS TIDE</div>
    <div class="artwork" role="img" aria-label="Hand-drawn fashion illustration of two figures with a small pet, hearts, stars and patterned fabric in cream, gold and violet tones">
      <span class="artwork__band"></span>
    </div>
    <p class="tagline">Purveyors of inspiration &amp; Opportunity</p>
  </section>

  <section class="card card--back" aria-label="Card back">
    <h1 class="holder__name">Nora Lindqvist-Tan</h1>
    <p class="holder__role">Partner &amp; Strategist</p>
    <svg class="divider" width="120" height="12" viewBox="0 0 120 12" aria-hidden="true">
      <line x1="0" y1="6" x2="50" y2="6" stroke="#111" stroke-width="1"/>
      <circle cx="60" cy="6" r="4" fill="#b77fb0"/>
      <line x1="70" y1="6" x2="120" y2="6" stroke="#111" stroke-width="1"/>
    </svg>
    <p class="services">Boutique development &amp; sourcing<br>Sustainability &amp; innovation</p>
    <svg class="divider" width="120" height="12" viewBox="0 0 120 12" aria-hidden="true">
      <line x1="0" y1="6" x2="50" y2="6" stroke="#111" stroke-width="1"/>
      <circle cx="60" cy="6" r="4" fill="#b77fb0"/>
      <line x1="70" y1="6" x2="120" y2="6" stroke="#111" stroke-width="1"/>
    </svg>
    <p class="contact">+852 5550 1847<br>nora@mosstide.asia<br>www.mosstide.asia</p>
  </section>
</main>
</body>
</html>
```